High-End audio shop owner needs a business card

I need a personal Business Card for my Audio shop which exists since 1962. We offer high Quality brands, professional Attention and run our own repair-service-department. I look for a design which will be printed on high Quality paper and shall convey trust to the Client that we are very serious. Language is german.

```html
<!DOCTYPE html>
<html lang="de">
<head>
<meta charset="utf-8">
<title>Hi-Fi Talmann – Visitenkarte</title>
<link href="https://fonts.googleapis.com/css2?family=Work+Sans:wght@400;500;800&display=swap" rel="stylesheet">
<style>
  :root {
    --backdrop: #161616;
    --card: #262626;
    --card-edge: #2e2e2e;
    --orange: #f26b1d;
    --silver: #cfcfcf;
    --ink: #f2f2f2;
  }
  * { margin: 0; padding: 0; box-sizing: border-box; }
  html, body {
    width: 1200px; height: 900px; overflow: hidden;
    background: var(--backdrop);
    font-family: "Work Sans", Arial, sans-serif;
  }
  .stage {
    width: 1200px; height: 900px;
    display: flex; flex-direction: column; align-items: center; justify-content: center;
    gap: 40px;
  }
  .card {
    width: 700px; height: 400px;
    background: linear-gradient(135deg, var(--card) 0%, #2c2c2c 60%, #232323 100%);
    border: 1px solid var(--card-edge);
    position: relative;
    box-shadow: 0 12px 30px rgba(0,0,0,.5);
  }
  .card--front { display: flex; align-items: center; justify-content: center; }
  .brand-name {
    font-weight: 800; font-size: 52px; letter-spacing: 2px; text-transform: uppercase;
    white-space: nowrap;
  }
  .card--front .brand-name { color: var(--silver); }
  .card--back .brand-name {
    color: var(--orange); font-size: 32px; letter-spacing: 1px;
    position: absolute; left: 50px; top: 182px;
  }
  .divider {
    position: absolute; left: 370px; top: 110px;
    width: 2px; height: 190px; background: var(--orange);
  }
  .contact {
    position: absolute; left: 400px; top: 100px;
    color: var(--ink); font-size: 17px; line-height: 1.45; letter-spacing: .5px;
  }
  .contact__name {
    color: var(--orange); font-weight: 500; font-size: 27px; letter-spacing: 1px;
    line-height: 1.1; white-space: nowrap;
  }
  .contact__role { font-size: 17px; margin-bottom: 14px; }
  .contact__address { margin-bottom: 4px; }
  .contact__line { display: flex; align-items: center; gap: 8px; white-space: nowrap; }
  .contact__line svg { width: 13px; height: 13px; flex: none; }
</style>
</head>
<body>
<main class="stage">
  <section class="card card--front">
    <div class="brand-name">Hi-Fi Talmann</div>
  </section>

  <section class="card card--back">
    <div class="brand-name">Hi-Fi Talmann</div>
    <div class="divider"></div>
    <div class="contact">
      <div class="contact__name">DANIEL BRANDT</div>
      <div class="contact__role">Director</div>
      <div class="contact__address">2217 Cedar Mill<br>Road Boise, ID 83706</div>
      <div class="contact__line">
        <svg viewBox="0 0 16 16" aria-hidden="true"><path d="M4 1 6.5 4 5 6c1 2 3 4 5 5l2-1.5 3 2.5-1.5 2.5C8 15 1 8 1.5 2.5Z" fill="var(--orange)"/></svg>
        208-555-0147
      </div>
      <div class="contact__line">
        <svg viewBox="0 0 16 16" aria-hidden="true"><rect x="1.5" y="3.5" width="13" height="9" fill="none" stroke="var(--orange)" stroke-width="1.5"/><path d="M1.5 3.5 8 9l6.5-5.5" fill="none" stroke="var(--orange)" stroke-width="1.5"/></svg>
        info@hifitalmann.com
      </div>
      <div class="contact__line">
        <svg viewBox="0 0 16 16" aria-hidden="true"><circle cx="8" cy="8" r="6.5" fill="none" stroke="var(--orange)" stroke-width="1.4"/><ellipse cx="8" cy="8" rx="3" ry="6.5" fill="none" stroke="var(--orange)" stroke-width="1.2"/><path d="M1.5 8h13" stroke="var(--orange)" stroke-width="1.2"/></svg>
        www.hifitalmann.com
      </div>
    </div>
  </section>
</main>
</body>
</html>
```